Dietitian needs a new business card design

I need a new business card design for my nutrition business that provides individual clinical nutrition advice for people with medical conditions. Business cards will be handed out to doctors, specialists and clients so will need to be sharp and project an image of professionalism

Target Market(s)

My clients are typically referred by doctors or specialists and the card will be used to handout to clients and their doctors.

Industry/Entity Type

Medical

Contact Information for Business Card

The business card will require the details below. These details can be found from my website https://www.kelvarrowclinic.com.au/

Font styles to use
Serif

Colors

Designer to choose colors to be used in the design.

Requirements
Must have
• 1. It needs be professional and contemporary
• 2. It needs to incorporate my logo
• 3. It needs space to write appointment times and dates
• 4. It needs to provide my phone number, fax number, email address and my web address
Nice to have
• Include the Registered Tovance Clinician Logo
• I have access to Framellow if required
• The locations I practise from
Should not have
• Pictures of food
• Spelling MIstakes

```html
<!DOCTYPE html>
<html lang="en">
<head>
<meta charset="utf-8">
<title>Kelvarrow Nutrition &amp; Dietetics – Business Card</title>
<link rel="stylesheet" href="https://fonts.googleapis.com/css2?family=Roboto:wght@400;500&display=swap">
<style>
  :root {
    --backdrop: #e6e6e6;
    --card: #f7f7f6;
    --ink: #4a4a4a;
    --ink-strong: #5e5e5e;
    --brand-blue: #1f63b4;
    --green-light: #c8dc2c;
    --green-mid: #8cc63e;
    --green-deep: #5fb247;
    --blue-deep: #1557a8;
    --rule: #6b6b6b;
  }
  * { margin: 0; padding: 0; box-sizing: border-box; }
  html, body { width: 1200px; height: 960px; overflow: hidden; }
  body {
    background: var(--backdrop);
    position: relative;
    font-family: "Roboto", Arial, sans-serif;
    color: var(--ink);
  }
  .card {
    position: absolute;
    width: 600px;
    height: 343px;
    background: var(--card);
    border-radius: 18px;
    overflow: hidden;
    box-shadow: 0 2px 6px rgba(0,0,0,0.18);
  }
  .card--front { left: 314px; top: 113px; }
  .card--back { left: 311px; top: 472px; }

  .front-info { position: absolute; left: 28px; top: 26px; }
  .brand-name {
    font-weight: 400;
    color: var(--brand-blue);
    font-size: 40px;
    line-height: 44px;
    letter-spacing: -0.5px;
  }
  .brand-tag {
    font-weight: 400;
    color: var(--brand-blue);
    font-size: 19px;
    line-height: 22px;
  }
  .person-name {
    margin-top: 16px;
    font-size: 21px;
    font-weight: 500;
    color: var(--ink-strong);
    line-height: 24px;
  }
  .person-title { font-size: 15px; color: var(--ink-strong); line-height: 18px; }
  .locations { margin-top: 12px; font-size: 14px; line-height: 18px; }
  .contacts { margin-top: 7px; list-style: none; font-size: 14px; line-height: 19.5px; }
  .contacts li { display: flex; align-items: center; gap: 8px; }
  .contacts svg { width: 14px; height: 14px; fill: var(--ink-strong); flex: none; }

  .brand-field { position: absolute; right: 0; top: 0; width: 322px; height: 343px; }

  .back-brand {
    position: absolute; top: 50px; left: 0; width: 100%;
    display: flex; justify-content: center; align-items: center; gap: 12px;
  }
  .back-brand .dot { width: 40px; height: 40px; border-radius: 50%; background: var(--green-mid); }
  .back-brand .name { font-size: 28px; color: var(--brand-blue); line-height: 30px; }

  .appointments { position: absolute; left: 80px; top: 138px; width: 440px; }
  .appt-row { display: flex; align-items: baseline; height: 45px; font-size: 15px; }
  .appt-row .blank { border-bottom: 1px solid var(--rule); height: 1px; margin: 0 6px 0 4px; align-self: center; transform: translateY(6px); }
  .blank--date { width: 186px; margin-right: 18px !important; }
  .blank--time { width: 102px; }

  .back-footer {
    position: absolute; left: 0; width: 100%; top: 283px;
    text-align: center; font-size: 14px; line-height: 18px;
  }
</style>
</head>
<body>

<section class="card card--front">
  <div class="front-info">
    <div class="brand-name">Kelvarrow</div>
    <div class="brand-tag">Nutrition &amp; Dietetics</div>
    <div class="person-name">Daniel Ashcombe</div>
    <div class="person-title">Accredited Nutritionist</div>
    <div class="locations">
      Brindlewood Medical Centre<br>
      Fernhollow Medical<br>
      East Corran Health<br>
      Pellbridge Doctors Surgery
    </div>
    <ul class="contacts">
      <li><svg viewBox="0 0 24 24"><path d="M6.6 10.8a15 15 0 0 0 6.6 6.6l2.2-2.2a1 1 0 0 1 1-.25 11.4 11.4 0 0 0 3.6.57 1 1 0 0 1 1 1V20a1 1 0 0 1-1 1A17 17 0 0 1 3 4a1 1 0 0 1 1-1h3.5a1 1 0 0 1 1 1c0 1.25.2 2.45.57 3.57a1 1 0 0 1-.25 1z"/></svg>0400 555 182</li>
      <li><svg viewBox="0 0 24 24"><path d="M6 3h12v5H6zM3 9h18v9h-3v3H6v-3H3zm5 6v4h8v-4z"/></svg>+613 5550 4417</li>
      <li><svg viewBox="0 0 24 24"><path d="M3 5h18v14H3zm2 2v.5l7 4.5 7-4.5V7z"/></svg>dan@kelvarrowclinic.com.au</li>
      <li><svg viewBox="0 0 24 24"><path d="M12 2a10 10 0 1 0 0 20 10 10 0 0 0 0-20zm5.9 9h-3a15 15 0 0 0-1.2-6 8 8 0 0 1 4.2 6zM12 4.1c.9 1.3 1.7 3.8 1.9 6.9h-3.8c.2-3.1 1-5.6 1.9-6.9zM10.3 5a15 15 0 0 0-1.2 6h-3a8 8 0 0 1 4.2-6zM6.1 13h3a15 15 0 0 0 1.2 6 8 8 0 0 1-4.2-6zm5.9 6.9c-.9-1.3-1.7-3.8-1.9-6.9h3.8c-.2 3.1-1 5.6-1.9 6.9zm1.7-.9a15 15 0 0 0 1.2-6h3a8 8 0 0 1-4.2 6z"/></svg>www.kelvarrowclinic.com.au</li>
    </ul>
  </div>

  <svg class="brand-field" viewBox="0 0 322 343" role="img" aria-label="Brand artwork area in blue and green tones">
    <defs>
      <linearGradient id="fieldTone" x1="0" y1="0" x2="1" y2="1">
        <stop offset="0" stop-color="var(--blue-deep)" stop-opacity="0.85"/>
        <stop offset="0.45" stop-color="var(--green-deep)"/>
        <stop offset="1" stop-color="var(--green-light)"/>
      </linearGradient>
    </defs>
    <rect x="0" y="0" width="322" height="343" fill="url(#fieldTone)"/>
  </svg>
</section>

<section class="card card--back">
  <div class="back-brand">
    <span class="dot"></span>
    <span class="name">Kelvarrow Nutrition &amp; Dietetics</span>
  </div>

  <div class="appointments">
    <div class="appt-row"><span>Date</span><span class="blank blank--date"></span><span>Time</span><span class="blank blank--time"></span><span>am/pm</span></div>
    <div class="appt-row"><span>Date</span><span class="blank blank--date"></span><span>Time</span><span class="blank blank--time"></span><span>am/pm</span></div>
    <div class="appt-row"><span>Date</span><span class="blank blank--date"></span><span>Time</span><span class="blank blank--time"></span><span>am/pm</span></div>
  </div>

  <div class="back-footer">
    Dietitian for Kelvarrow &amp; the North East Coast<br>
    Pellbridge Doctors Surgery
  </div>
</section>

</body>
</html>
```